Harbin Motors LLC

Car Dealer Customer Service
Address: 2847 Calloway Avenue, Shelbyville, TN 37160
web: www.harbinmotorsco.example
email: harbinmotorsco@mailbox.example
Phone: (931) 555-0147
Phone: (629) 555-0183

```html
<!DOCTYPE html>
<html lang="en">
<head>
<meta charset="utf-8">
<title>Harbin Motors — Business Card</title>
<link href="https://fonts.googleapis.com/css2?family=Arimo:wght@400&family=Cormorant+Garamond:ital,wght@1,600&family=Montserrat:wght@800&display=swap" rel="stylesheet">
<style>
  :root {
    --backdrop: #9c9c9c;
    --gold: #ebb348;
    --blue: #1a77a8;
    --white: #ffffff;
    --rule: #6fa9c9;
  }
  * { margin: 0; padding: 0; box-sizing: border-box; }
  html, body { width: 1200px; height: 1200px; overflow: hidden; }
  body { background: var(--backdrop); position: relative; font-family: "Arimo", Arial, sans-serif; }

  .card { position: absolute; top: 303px; width: 368px; height: 594px; overflow: hidden; }
  .card--front { left: 200px; background: var(--blue); }
  .card--back { left: 599px; background: var(--blue); }

  /* front */
  .front-top { position: absolute; left: 0; top: 0; width: 100%; height: 439px; background: var(--gold); }
  .tagline {
    position: absolute; left: 0; width: 100%; text-align: center;
    font-family: "Cormorant Garamond", Georgia, serif; font-style: italic; font-weight: 600;
    font-size: 60px; line-height: 86px; color: var(--white); top: 44px;
  }
  .tagline span { display: block; }
  .car-art {
    position: absolute; left: 14px; top: 327px; width: 354px; height: 131px;
    background: linear-gradient(180deg, #fbf3e1 0%, #ffffff 100%); border-radius: 60px 40px 30px 30px;
  }
  .front-brand {
    position: absolute; left: 0; top: 494px; width: 100%; text-align: center;
    font-family: "Montserrat", Arial, sans-serif; font-weight: 800; font-size: 29px;
    letter-spacing: 0.5px; color: var(--white); text-transform: uppercase;
  }

  /* back */
  .back-top { position: absolute; left: 0; top: 0; width: 100%; height: 290px; background: var(--white); }
  .back-stripe { position: absolute; left: 0; top: 290px; width: 100%; height: 6px; background: var(--gold); }
  .brand-dot { position: absolute; left: 129px; top: 86px; width: 110px; height: 110px; border-radius: 50%; background: var(--blue); }
  .back-brand {
    position: absolute; left: 0; top: 220px; width: 100%; text-align: center;
    font-family: "Montserrat", Arial, sans-serif; font-weight: 800; font-size: 28px;
    color: var(--blue); text-transform: uppercase;
  }
  .person-name {
    position: absolute; left: 0; top: 326px; width: 100%; text-align: center;
    font-family: "Montserrat", Arial, sans-serif; font-weight: 800; font-size: 20px;
    color: var(--white); text-transform: uppercase;
  }
  .person-role { position: absolute; left: 0; top: 349px; width: 100%; text-align: center; font-size: 16px; color: var(--white); }
  .icon-row { position: absolute; left: 0; top: 378px; width: 100%; display: flex; justify-content: center; align-items: center; gap: 5px; }
  .icon-row .line { width: 32px; height: 1px; background: var(--rule); margin: 0 6px; }
  .icon { width: 25px; height: 25px; background: var(--white); border-radius: 3px; display: flex; align-items: center; justify-content: center; }
  .contacts { position: absolute; left: 0; top: 414px; width: 100%; text-align: center; color: var(--white); font-size: 16.5px; line-height: 21.6px; }
  .divider { position: absolute; left: 88px; top: 513px; width: 192px; height: 1px; background: var(--rule); }
  .address { position: absolute; left: 0; top: 521px; width: 100%; text-align: center; color: var(--white); font-size: 16.5px; line-height: 21.6px; }
</style>
</head>
<body>
  <section class="card card--front">
    <div class="front-top"></div>
    <h1 class="tagline"><span>Car Dealer</span><span>Customer</span><span>Service</span></h1>
    <div class="car-art" role="img" aria-label="White vintage car illustration"></div>
    <div class="front-brand">Harbin Motors</div>
  </section>

  <section class="card card--back">
    <div class="back-top"></div>
    <div class="back-stripe"></div>
    <div class="brand-dot"></div>
    <div class="back-brand">Harbin Motors</div>
    <div class="person-name">Daniel Whitfield</div>
    <div class="person-role">Managing Director</div>
    <div class="icon-row">
      <span class="line"></span>
      <span class="icon"><svg width="17" height="17" viewBox="0 0 24 24"><path fill="#1a77a8" d="M3 9c0-3 4-5 9-5s9 2 9 5v2h-4V9c0-1-2-2-5-2S7 8 7 9v2H3zm4 4h10l2 7H5z"/></svg></span>
      <span class="icon"><svg width="17" height="17" viewBox="0 0 24 24"><path fill="#1a77a8" d="M3 9c0-3 4-5 9-5s9 2 9 5v2h-4V9c0-1-2-2-5-2S7 8 7 9v2H3zm4 4h10l2 7H5z"/></svg></span>
      <span class="icon"><svg width="17" height="17" viewBox="0 0 24 24"><circle cx="12" cy="12" r="9" fill="#1a77a8"/><path d="M3 12h18M12 3c3 3 3 15 0 18M12 3c-3 3-3 15 0 18" stroke="#fff" stroke-width="1.3" fill="none"/></svg></span>
      <span class="icon"><svg width="17" height="17" viewBox="0 0 24 24"><rect x="3" y="6" width="18" height="12" fill="#1a77a8"/><path d="M3 6l9 7 9-7M3 18l7-6M21 18l-7-6" stroke="#fff" stroke-width="1.2" fill="none"/></svg></span>
      <span class="line"></span>
    </div>
    <div class="contacts">
      (931) 555-0147<br>
      (629) 555-0183<br>
      www.harbinmotorsco.example<br>
      harbinmotorsco@mailbox.example
    </div>
    <div class="divider"></div>
    <div class="address">2847 Calloway Avenue<br>Shelbyville, TN 37160</div>
  </section>
</body>
</html>
```